Membership Comparison Chart

I need the current membership chart recreated with additional perks listed at the bottom with our other companies, when you purchase a membership with us. Please remove the "curated cafe" at the bottom (has not opened yet). We are a shooting range and education center. This chart was originally created 2 years ago. I need in file form that is printable as well as a file that is able to be updated periodically. Please add the words "A Vantrop Group Company" below the logo attached.

```html
<!DOCTYPE html>
<html lang="en">
<head>
<meta charset="utf-8">
<title>Membership Comparison Chart</title>
<link rel="stylesheet" href="https://fonts.googleapis.com/css2?family=Oswald:wght@600;700&family=Roboto+Condensed:ital,wght@0,700;1,600&family=Open+Sans:ital,wght@0,400;0,600;0,700;0,800;1,400;1,600;1,800&display=swap">
<style>
:root{
  --ink:#111;
  --black:#0c0c0c;
  --white:#fff;
  --red:#e3262b;
  --row-alt:#efefef;
  --rule:#c9c9c9;
  --basic:#29b3e6;
  --elite:#e3212a;
  --platinum:#f5b419;
  --muted:#444;
}
*{box-sizing:border-box;margin:0;padding:0}
html,body{width:960px;height:1200px;overflow:hidden;background:var(--white)}
body{font-family:"Open Sans",Arial,sans-serif;color:var(--ink);position:relative}

.top-band{position:absolute;left:0;top:0;width:960px;height:200px;background:var(--black)}
.headline{position:absolute;left:48px;top:34px;width:870px;color:var(--white);
  font-family:"Roboto Condensed",Arial Narrow,sans-serif;font-style:italic;font-weight:600;
  font-size:29px;line-height:36px;letter-spacing:-.2px}

.chart{position:absolute;left:48px;top:122px;width:864px}
.chart-head{display:grid;grid-template-columns:278px 195px 195px 196px;height:88px}
.brand-cell{background:var(--white);border:1px solid var(--rule);display:flex;flex-direction:column;justify-content:center;padding:0 20px 0 26px;margin-top:18px}
.brand-line{display:flex;align-items:center;gap:9px}
.brand-dot{width:30px;height:30px;border-radius:50%;background:var(--red);flex:none}
.brand-name{font-weight:700;font-size:14px;line-height:16px;color:var(--ink);text-transform:uppercase}
.brand-parent{margin:5px 0 0 39px;font-size:10px;font-weight:600;color:var(--ink);text-transform:uppercase;letter-spacing:.2px}

.tier{display:flex;flex-direction:column;background:var(--black);border-left:1px solid #333}
.tier-tab{height:42px;display:flex;align-items:center;justify-content:center;
  font-family:"Oswald",Impact,sans-serif;font-weight:700;font-size:33px;color:var(--white);letter-spacing:.5px;
  clip-path:polygon(0 0,100% 0,95% 100%,5% 100%);margin:0 -2px}
.tier-basic .tier-tab{background:var(--basic)}
.tier-elite .tier-tab{background:var(--elite)}
.tier-platinum .tier-tab{background:var(--platinum)}
.tier-label{flex:1;display:flex;align-items:center;justify-content:center;color:var(--white);font-weight:600;font-size:14px;letter-spacing:.3px}

.row{display:grid;grid-template-columns:278px 195px 195px 196px;height:43px;border-bottom:1px solid var(--rule);border-left:1px solid var(--rule);border-right:1px solid var(--rule)}
.row:nth-child(even){background:var(--row-alt)}
.row > div{display:flex;flex-direction:column;justify-content:center;border-right:1px solid var(--rule)}
.row > div:last-child{border-right:0}
.feature{padding-left:12px;font-weight:700;font-size:13px;line-height:15px}
.feature small{display:block;font-weight:400;font-style:italic;font-size:10px;line-height:12px}
.value{align-items:center;text-align:center;color:var(--red);font-weight:700;font-size:15px;line-height:16px;text-transform:uppercase}
.value small{color:var(--ink);font-size:10px;font-weight:700;line-height:13px}
.value.tight{font-size:13px;line-height:14px}
.tick{width:26px;height:22px}
.no-hold{flex-direction:row!important;align-items:center;justify-content:flex-start!important;gap:6px}
.no-hold b{font-size:30px;font-weight:800;line-height:1}
.no-hold span{font-size:12px;font-weight:600;line-height:14px}

.row.cost{height:92px}
.cost .feature{font-weight:600;font-size:13px;line-height:17px}
.cost .feature small{font-size:10px}
.cost .value{font-size:15px;line-height:16px}
.cost .value small{margin-bottom:6px}

.extras-title{position:absolute;left:0;top:918px;width:960px;text-align:center;font-weight:800;font-style:italic;font-size:31px;letter-spacing:-.3px}
.extras{position:absolute;left:49px;top:968px;display:grid;grid-template-columns:254px 218px 151px 218px;gap:7px;height:190px}
.perk{border:1px solid var(--rule);display:flex;flex-direction:column;align-items:center;text-align:center;font-size:11px;font-weight:700;line-height:13px;text-transform:uppercase;padding:10px}
.perk-stack{display:grid;grid-template-rows:1fr 1fr;gap:7px}
.perk-stack .perk{flex-direction:row;text-align:center;gap:12px;padding:8px 12px}
.partner-badge{width:64px;height:64px;border-radius:50%;background:#222;flex:none}
.partner-name{font-weight:700;font-size:13px;line-height:15px;color:var(--ink);letter-spacing:1px;flex:none;width:84px}
.perk-stack .perk p{flex:1}
.verdant .brand-line{gap:8px;margin:12px 0 26px}
.verdant-mark{width:40px;height:40px;background:#7dc242;flex:none}
.verdant .partner-title{font-size:17px;line-height:18px;text-align:left;font-weight:800}
.perk p + p{margin-top:8px}
.fairmont .partner-title{font-size:19px;line-height:21px;font-weight:700;margin-top:4px}
.fairmont .partner-sub{font-size:10px;font-weight:600;margin-top:3px}
.fairmont .big-offer{color:var(--red);font-size:33px;font-weight:800;line-height:36px;margin-top:22px}
.promise .brand-line{margin-top:4px}
.promise .brand-dot{width:24px;height:24px}
.promise .brand-name{font-size:12px;line-height:13px;text-align:left}
.promise .brand-parent{margin:3px 0 0;font-size:8px}
.promise h3{font-family:"Oswald",Impact,sans-serif;font-size:30px;line-height:34px;font-weight:600;margin-top:6px}
.promise p{font-size:10px;line-height:12px;text-transform:none}
</style>
</head>
<body>
<div class="top-band"></div>
<h1 class="headline">Featuring the World’s Largest indoor Double-deck Gun Range, Digital Assault Survival Theater, and 20+ Safety-Focused Classes, our membership gives you unbeatable value...</h1>

<section class="chart">
  <div class="chart-head">
    <div class="brand-cell">
      <div class="brand-line"><span class="brand-dot"></span><span class="brand-name">Kestrel Ridge<br>Shooting Center</span></div>
      <div class="brand-parent">A Vantrop Group Company</div>
    </div>
    <div class="tier tier-basic"><div class="tier-tab">BASIC</div><div class="tier-label">MEMBERSHIP</div></div>
    <div class="tier tier-elite"><div class="tier-tab">ELITE</div><div class="tier-label">MEMBERSHIP</div></div>
    <div class="tier tier-platinum"><div class="tier-tab">PLATINUM</div><div class="tier-label">MEMBERSHIP</div></div>
  </div>

  <div class="rows">
    <div class="row"><div class="feature">Family Gun &amp; Archery Range Use<small>You, your spouse and all children under 18. 21 Gun Salute Range and Archery Range</small></div><div class="value">Free<small>UNLIMITED USE</small></div><div class="value">Free<small>UNLIMITED USE</small></div><div class="value">Free<small>UNLIMITED USE</small></div></div>
    <div class="row"><div class="feature">FREE Firearm Lesson<small>Level tailored to your experience</small></div><div class="value"></div><div class="value">Free Lesson</div><div class="value">Free Lesson</div></div>
    <div class="row"><div class="feature">FREE Archery Lesson<small>Level tailored to your experience</small></div><div class="value"></div><div class="value">Free Lesson</div><div class="value">Free Lesson</div></div>
    <div class="row"><div class="feature">50% OFF All Firearms</div><div class="value"></div><div class="value tight">Stock and<br>Special Order</div><div class="value tight">Stock and<br>Special Order</div></div>
    <div class="row"><div class="feature">Digital Assault Survival and Fun Target Theaters</div><div class="value">25% Off</div><div class="value">50% Off</div><div class="value">Free 12 Hours</div></div>
    <div class="row"><div class="feature">10% OFF Everything Else<small>(Ammo, Holsters, Targets, Gun Bags, etc.)</small></div><div class="value">10% Off</div><div class="value">10% Off</div><div class="value">10% Off</div></div>
    <div class="row"><div class="feature">Required Master Carrier Target</div><div class="value">10% Off</div><div class="value">10% Off</div><div class="value tight">1Free<br>Every Visit</div></div>
    <div class="row"><div class="feature">Discounts on KRSC Training*<small>Dozens of Basic and Advanced Classes</small></div><div class="value">25% Off</div><div class="value">50% Off<small>PLUS 2 FREE REPEATS</small></div><div class="value">Free Unlimited<small>PLUS 10 FREE REPEATS</small></div></div>
    <div class="row"><div class="feature">FREE Guest Passes Per Year Sharing Lane with Member</div><div class="value">5 Free Yearly</div><div class="value">10 Free Yearly</div><div class="value">1 Free Per Visit<small>PLUS 10 FREE FOR GIFTING*</small></div></div>
    <div class="row"><div class="feature">Gun Rentals</div><div class="value">50% Off</div><div class="value">50% Off</div><div class="value">Free<small>FOR MEMBERS &amp; GUESTS</small></div></div>
    <div class="row"><div class="feature">Discount on FFL Transfer</div><div class="value">$10 Off</div><div class="value">$15 Off</div><div class="value">Free Unlimited</div></div>
    <div class="row"><div class="feature no-hold"><b>No</b><span>Credit Card Hold for Lanes<br>Firearm Deposit Required</span></div>
      <div class="value"><svg class="tick" viewBox="0 0 26 22" aria-hidden="true"><path d="M2 12 L10 19 L24 3" fill="none" stroke="#e3262b" stroke-width="4.5" stroke-linecap="round" stroke-linejoin="round"/></svg></div>
      <div class="value"><svg class="tick" viewBox="0 0 26 22" aria-hidden="true"><path d="M2 12 L10 19 L24 3" fill="none" stroke="#e3262b" stroke-width="4.5" stroke-linecap="round" stroke-linejoin="round"/></svg></div>
      <div class="value"><svg class="tick" viewBox="0 0 26 22" aria-hidden="true"><path d="M2 12 L10 19 L24 3" fill="none" stroke="#e3262b" stroke-width="4.5" stroke-linecap="round" stroke-linejoin="round"/></svg></div></div>
    <div class="row"><div class="feature">Meeting/Party Room</div><div class="value">1 Hour</div><div class="value">5 Hours</div><div class="value">10 Hours</div></div>
    <div class="row"><div class="feature">REFER New Member Reward</div><div class="value">$10 Gift Card</div><div class="value">$20 Gift Card</div><div class="value">$25 Gift Card</div></div>
    <div class="row cost"><div class="feature">COST<br>Plus 1-time $100 initiation Fee<small>(No Fee if Paid in full with Cash)</small></div>
      <div class="value">$35 Per Month<small>$520 TOTAL</small>Single Payment<small>$420 TOTAL</small></div>
      <div class="value">$55 Per Month<small>$760 TOTAL</small>Single Payment<small>$660 TOTAL</small></div>
      <div class="value">$79 Per Month<small>$1048 TOTAL</small>Single Payment<small>$948 TOTAL</small></div></div>
  </div>
</section>

<h2 class="extras-title">....plus these extra benefits you never expected.</h2>

<section class="extras">
  <div class="perk-stack">
    <div class="perk"><span class="partner-badge" role="img" aria-label="Lakeshore Pickleball Center badge"></span><p>5 Free Outdoor Indoor Court Passes (Punch Card)</p></div>
    <div class="perk"><span class="partner-name">HILLCREST VENUE</span><p>5% Off Social Events and Wedding Packages (Venue Rental)</p></div>
  </div>
  <div class="perk verdant">
    <div class="brand-line"><span class="verdant-mark"></span><span class="partner-title">VERDANT<br>YARD CO</span></div>
    <p>50% Off Delivery Fee for Mulch, Stone, Topsoil.</p>
    <p>50% Off Concrete, Basement Waterproofing, Snow Mitigation, or Lawn Care</p>
  </div>
  <div class="perk fairmont">
    <div class="partner-title">FAIRMONT INDUSTRIAL</div>
    <div class="partner-sub">Technology Center</div>
    <div class="big-offer">10% OFF</div>
    <p>First Month Payment with a 1-Year Lease</p>
  </div>
  <div class="perk promise">
    <div class="brand-line"><span class="brand-dot"></span><div><div class="brand-name">Kestrel Ridge Shooting Center</div><div class="brand-parent">A Vantrop Group Company</div></div></div>
    <h3>OUR PROMISE</h3>
    <p>We will do everything in our power to support our members’ wellness health, and safety with education and training in a state-of-the-art facility.</p>
  </div>
</section>
</body>
</html>
```